Quill|Marlow & Petrie business card contest

We need a logo for an upscale boutique diversified company involved in real estate, investments, cattle, and more. Our businesses DO NOT need to be reflected in the business card nor do we want them noted. This is our logo and colors and we love our logo and colors. Our logo looks best against a black background and we like to include the firm name in our logo usage. importantly, the names Quill and Marlow are separated by | not / and we use an ampersand not the word and.
On the front of the card, we want to include:
company logo and name (Quill|Marlow & Petrie)
on the back, we would definitely include:
address, email, cell #
logo and name (smaller size than front)

The variable will be location of individual name and title (mine for example is ) - whether on the front OR on the back. interested in variations from which to choose
Dr. Owen T. Caldecott, CFA
Scientifique des Fusées Financières

we would like to use contemporary symbols for address, email address, cell # with an option for web site that we do not intend to use initially. we like two sided cards and believe this design should use four rounded corners with the standard size. we prefer thicker card stock and may look at metal.

```html
<!DOCTYPE html>
<html lang="en">
<head>
<meta charset="utf-8">
<title>Quill|Marlow &amp; Petrie — Business Card</title>
<link href="https://fonts.googleapis.com/css2?family=Raleway:wght@400;500&family=Source+Sans+3:wght@400&display=swap" rel="stylesheet">
<style>
  :root {
    --backdrop: #222629;
    --card-light: #f3f3f3;
    --brand-orange: #d8762a;
    --ink-grey: #5a5a5a;
    --ink-soft: #555555;
  }
  * { box-sizing: border-box; margin: 0; padding: 0; }
  html, body {
    width: 1200px; height: 1176px; overflow: hidden;
    background: var(--backdrop);
  }
  .canvas { position: relative; width: 1200px; height: 1176px; }
  .card {
    position: absolute; left: 281px; width: 616px; height: 352px;
    border-radius: 22px;
  }
  .card--front { top: 190px; background: var(--card-light); }
  .card--back  { top: 591px; background: var(--brand-orange); }

  .brand {
    position: absolute; display: flex; flex-direction: column; align-items: center;
    font-family: "Raleway", sans-serif; font-weight: 500; color: var(--ink-grey);
    white-space: nowrap;
  }
  .brand__square { background: var(--brand-orange); }
  .card--front .brand { left: 30px; width: 220px; top: 118px; }
  .card--front .brand__square { width: 60px; height: 60px; margin-bottom: 18px; }
  .card--front .brand__name { font-size: 19px; }
  .card--back .brand { left: 0; width: 616px; top: 82px; }
  .card--back .brand__square { width: 94px; height: 94px; margin-bottom: 26px; background: var(--ink-grey); }
  .card--back .brand__name { font-size: 34px; }

  .divider {
    position: absolute; left: 272px; top: 101px; width: 2px; height: 150px;
    background: var(--brand-orange);
  }
  .details { position: absolute; left: 296px; top: 112px; }
  .details__name {
    font-family: "Raleway", sans-serif; font-weight: 400; font-size: 19px;
    color: var(--ink-grey); text-transform: uppercase; line-height: 1;
  }
  .details__name small { font-size: 14px; }
  .details__title {
    font-family: "Raleway", sans-serif; font-weight: 400; font-size: 13.5px;
    color: var(--brand-orange); text-transform: uppercase; margin-top: 7px;
  }
  .contact { list-style: none; margin-top: 14px; }
  .contact__item {
    display: flex; align-items: center; gap: 8px; height: 24.5px;
    font-family: "Source Sans 3", sans-serif; font-size: 14.5px; color: var(--ink-soft);
  }
  .contact__icon { width: 11px; height: 12px; fill: var(--brand-orange); flex: none; }
</style>
</head>
<body>
<main class="canvas">
  <section class="card card--front">
    <div class="brand">
      <div class="brand__square"></div>
      <div class="brand__name">Quill|Marlow &amp; Petrie</div>
    </div>
    <div class="divider"></div>
    <div class="details">
      <h1 class="details__name">Dr. Owen T. Caldecott, <small>CFA</small></h1>
      <p class="details__title">Scientifique des Fusées Financières</p>
      <ul class="contact">
        <li class="contact__item">
          <svg class="contact__icon" viewBox="0 0 11 12" aria-hidden="true"><path d="M3 0 L5 3 L3.6 4.6 Q4.6 7.4 6.8 8.6 L8.2 7.2 L11 9.4 L9.6 11.6 Q4.2 11.2 1 3.2 Q1.2 1 3 0 Z"/></svg>
          000 000 0000
        </li>
        <li class="contact__item">
          <svg class="contact__icon" viewBox="0 0 11 12" aria-hidden="true"><path d="M0 3 H11 V10 H0 Z M0.8 3.6 L5.5 7 L10.2 3.6" stroke="#f3f3f3" stroke-width="0.9"/></svg>
          youremail@xyz.com
        </li>
        <li class="contact__item">
          <svg class="contact__icon" viewBox="0 0 11 12" aria-hidden="true"><path d="M5.5 0.5 A3.8 3.8 0 0 1 9.3 4.3 Q9.3 6.8 5.5 11.5 Q1.7 6.8 1.7 4.3 A3.8 3.8 0 0 1 5.5 0.5 Z"/><circle cx="5.5" cy="4.3" r="1.4" fill="#f3f3f3"/></svg>
          000, Anywehre, Somewhere, City, ST 0000
        </li>
      </ul>
    </div>
  </section>

  <section class="card card--back">
    <div class="brand">
      <div class="brand__square"></div>
      <div class="brand__name">Quill|Marlow &amp; Petrie</div>
    </div>
  </section>
</main>
</body>
</html>
```